Restyle Company web site and logo

we need a wordpress design beacause after few year we need to refresh our company web site(www.vorantelabs.net) & logo. We are a small company called KP Advisory focused on business intellegence, data quality, data integration, etc and based on Legnago (small town near to Verona (italy)).
During the 2014 we add to our skill develop project for MDM and Procurement.
We are Young (avg 30 years old). We want to change our logo and color templete to communicate to all cumstomer professional skill, precision and passion.

--- UPDATE --
The new site can be complitile different from the actual website.
The new Logo is now available.
Updates

Target Market(s)

B2B, mid size market, professional account

Industry/Entity Type

It Company

Font styles to use
Sans Serif

Colors
acd037
3277b5

Requirements
Must have
• Simple and clean/clear image colur. Professional site. it need to rapresent trust site.
• Must be responsive desk/mobile.
Nice to have
• different color area for different kind off business line.
• slider image.
Should not have
• classical image

```html
<!DOCTYPE html>
<html lang="en">
<head>
<meta charset="utf-8">
<title>KP Advisory</title>
<link href="https://fonts.googleapis.com/css2?family=Arimo:wght@400&family=PT+Sans+Narrow:wght@400;700&family=Encode+Sans+Condensed:wght@300&family=Ubuntu:wght@400;500&display=swap" rel="stylesheet">
<style>
:root{
  --green:#8dc21f;
  --blue:#1f6fa8;
  --ink:#333;
  --text:#222;
  --band:#e3e1d6;
  --card:#f4f4f4;
  --footer:#353535;
  --footer-bottom:#2b2b2b;
  --footer-text:#b9b9b9;
  --caption:rgba(70,70,70,.92);
}
*{box-sizing:border-box;margin:0;padding:0}
html,body{width:960px;height:1200px;overflow:hidden;background:#fff}
body{position:relative;font-family:"Arimo",Arial,sans-serif;color:var(--text)}
.page{position:absolute;left:0;top:0;width:960px;height:1200px}

.brand{position:absolute;left:83px;top:44px;display:flex;align-items:center;gap:10px}
.brand-mark{width:26px;height:26px;background:var(--green)}
.brand-name{font-family:"Ubuntu",sans-serif;font-weight:500;font-size:24px;color:var(--blue)}

.main-nav{position:absolute;top:50px;left:394px;display:flex;align-items:center;font-family:"Ubuntu",sans-serif;font-weight:500;font-size:10.5px;color:var(--ink)}
.main-nav a{color:inherit;text-decoration:none;margin-right:31px}
.main-nav a.active{background:var(--green);color:#fff;padding:5px 15px;margin-right:16px}
.search{position:absolute;left:472px;top:-3px}

.slider{position:absolute;left:83px;top:121px;width:801px;height:307px}
.slide-photo{position:absolute;inset:0;background:linear-gradient(160deg,#d8d8d5 0%,#bfc4c2 40%,#8f9ea3 65%,#e9e9e6 100%)}
.dots{position:absolute;right:18px;top:10px;display:flex;gap:5px}
.dots span{width:8px;height:8px;background:#fff}
.dots span.on{background:var(--green)}
.caption{position:absolute;left:277px;top:124px;width:524px;height:147px;background:var(--caption);border-left:6px solid var(--green);padding:22px 26px 0 24px}
.caption h1{font-family:"Encode Sans Condensed",sans-serif;font-weight:300;font-size:48px;line-height:1;color:var(--green);letter-spacing:-.5px;white-space:nowrap}
.caption p{margin-top:10px;color:#fff;font-size:11px;line-height:14.5px}
.btn{display:inline-block;background:var(--green);color:#fff;font-size:10px;padding:5px 7px;text-decoration:none}
.caption .btn{position:absolute;right:0;bottom:0;padding:6px 7px}

.intro{position:absolute;left:83px;top:428px;width:801px;height:151px;background:var(--band);padding:20px 18px}
.intro h2{font-family:"PT Sans Narrow",sans-serif;font-weight:700;font-size:22px;line-height:25px;color:var(--ink)}
.intro p{margin-top:14px;font-size:10px;line-height:14.5px}

.news{position:absolute;top:614px;left:80px;width:804px;height:296px}
.card{position:absolute;top:0;width:204px;height:296px;padding:0 0 0 2px}
.card.shade{background:var(--card)}
.card h3{font-family:"PT Sans Narrow",sans-serif;font-weight:700;font-size:18px;line-height:20px;color:var(--ink);margin-top:10px;height:46px}
.card .thumb{width:188px;height:74px;margin-top:10px}
.card p{margin-top:15px;font-size:10px;line-height:14.5px;width:192px}
.card .btn{position:absolute;left:4px;bottom:9px}

.footer{position:absolute;left:84px;top:958px;width:799px;height:171px;background:var(--footer);color:var(--footer-text)}
.footer h4{font-family:"PT Sans Narrow",sans-serif;font-weight:700;color:#fff}
.f-about{position:absolute;left:18px;top:16px}
.f-about h4{font-size:16px}
.f-about address{font-style:normal;font-size:10px;line-height:14.5px;margin-top:5px}
.f-nav{position:absolute;left:418px;top:20px}
.f-nav h4{font-size:12px}
.f-nav ul{list-style:none;margin-top:7px;font-family:"Ubuntu",sans-serif;font-size:10px;line-height:17.5px}
.f-sub{position:absolute;left:582px;top:21px}
.f-sub h4{font-size:12px}
.signup{display:flex;margin-top:6px}
.signup .field{width:120px;height:25px;background:#4a4a4a;color:#888;font-size:10px;padding:6px 8px}
.signup .go{height:25px;background:var(--blue);color:#fff;font-family:"Ubuntu",sans-serif;font-weight:500;font-size:9.5px;padding:7px 9px}
.f-sub h4.community{margin-top:14px}
.social{display:flex;gap:4px;margin-top:10px}
.social span{width:20px;height:20px}
.legal{position:absolute;left:84px;top:1129px;width:799px;height:71px;background:var(--footer-bottom);color:var(--footer-text);font-size:10px;line-height:14.5px}
.legal .copy{position:absolute;left:25px;top:24px}
.legal .policy{position:absolute;right:21px;top:25px}
</style>
</head>
<body>
<div class="page">
  <header>
    <div class="brand"><span class="brand-mark"></span><span class="brand-name">KP Advisory</span></div>
    <nav class="main-nav">
      <a class="active" href="#">HOME</a>
      <a href="#">BUSINESS PARTNER</a>
      <a href="#">REFERENCE</a>
      <a href="#">WORK WITH US</a>
      <a href="#">CONTACT US</a>
      <svg class="search" width="17" height="17" viewBox="0 0 17 17" aria-label="Search"><circle cx="7" cy="7" r="5.5" fill="none" stroke="#333" stroke-width="2"/><line x1="11" y1="11" x2="16" y2="16" stroke="#333" stroke-width="2.2"/></svg>
    </nav>
  </header>

  <section class="slider">
    <div class="slide-photo" role="img" aria-label="Close-up of a business report with a pie chart and a pen"></div>
    <div class="dots"><span class="on"></span><span></span><span></span><span></span></div>
    <div class="caption">
      <h1>Business Intelligence</h1>
      <p>The information that drives your business. How many people in your company have the right information at the right time and in the correct form? KP Advisory helps you get all the information you need in the most...</p>
      <a class="btn" href="#">Read More</a>
    </div>
  </section>

  <section class="intro">
    <h2>How many people in your company have the desired information<br>at the right time and in the correct form?</h2>
    <p>For a company it is essential to exploit the wealth of information available to make them accessible to their managers in order to help them in choosing the right business strategies (see the trend of performance, generate estimates, assume future scenarios and future strategies of response.) KP Advisory helps you to manage this process as simple and fast!</p>
  </section>

  <section class="news">
    <article class="card" style="left:0">
      <h3>Lumen Report 2011</h3>
      <div class="thumb" role="img" aria-label="Team of smiling colleagues" style="background:linear-gradient(90deg,#c9d3d8,#e9ecee,#b8c4cc)"></div>
      <p>Lumen Solutions 2011 A comprehensive Business Intelligence level 1 How can you allow people to make better decisions faster and increase their productivity? Providing</p>
      <a class="btn" href="#">Read More</a>
    </article>
    <article class="card shade" style="left:199px">
      <h3>Event Tabula</h3>
      <div class="thumb" role="img" aria-label="Presenter speaking in a meeting room" style="background:linear-gradient(90deg,#6f6f6f,#c4c4c4,#5a5a5a)"></div>
      <p>The Management Control and Operational in Italy and Kessler Tabula KP Advisory, in collaboration with Kessler, invite you at the headquarters of our client at the seminar: "The Management Control and Operational in Kessler" 5</p>
      <a class="btn" href="#">Read More</a>
    </article>
    <article class="card" style="left:403px">
      <h3>Tabula Spring Tour 2012</h3>
      <div class="thumb" role="img" aria-label="Golfer on green rolling hills" style="background:linear-gradient(180deg,#b9d8ee 0%,#9cc65a 35%,#6aa22a 100%)"></div>
      <p>Tabula Italy is pleased to announce that in April will start the "Tabula Spring Tour 2012" that will visit eleven cities in the first phase of the 'northern Italy. A second ...</p>
      <a class="btn" href="#">Read More</a>
    </article>
    <article class="card shade" style="left:606px">
      <h3>Tabula wins the<br>Norvex .CORE Swiss Inno...</h3>
      <div class="thumb" role="img" aria-label="Innovation award badge" style="background:#fff"><svg width="188" height="74"><rect x="20" y="10" width="148" height="54" fill="#e6eef6"/></svg></div>
      <p>During the Norvex Tech Days 2010 Tabula has been recognized as the most innovative, high quality and easy to use, based on the latest Norvex technologies .CORE Lugano. Tabula International</p>
      <a class="btn" href="#">Read More</a>
    </article>
  </section>

  <footer class="footer">
    <div class="f-about">
      <h4>KP Advisory</h4>
      <address>Via dei Tigli, 12/B<br>37059 Borgoverde (VR)<br>Italy</address>
    </div>
    <div class="f-nav">
      <h4>Navigations</h4>
      <ul><li>HOME</li><li>BUSINESS PARTNER</li><li>REFERENCE</li><li>WORK WITH US</li><li>CONTACT US</li></ul>
    </div>
    <div class="f-sub">
      <h4>Subscribe Email Newsletter</h4>
      <div class="signup"><span class="field">Your Email</span><span class="go">SUBSCRIBE</span></div>
      <h4 class="community">Join Our Community</h4>
      <div class="social">
        <span style="background:#1da1d8" aria-label="Social profile"></span>
        <span style="background:#3b5c9e" aria-label="Social profile"></span>
        <span style="background:#1f7bbf" aria-label="Social profile"></span>
        <span style="background:#b3262a" aria-label="Social profile"></span>
      </div>
    </div>
  </footer>
  <div class="legal">
    <div class="copy">© Copyright KP Advisory S.r.l. 2014.<br>All Rights Reserved.</div>
    <div class="policy">Privacy Policy</div>
  </div>
</div>
</body>
</html>
```